Infographic for print (Graphic Customer Journey Cycle)

Hi guys,

We're looking for an infographic that we could print on an A4 leaflet.

I've attached the framework as PPT. We are looking for:
1. A circle layout where the images (please use icons or simple images) are in the inner circle; the titles of stages (New customer, Request more information, Receive offers etc.) are underneath the images; and the blocks of text are in an outer circle around the images. Please make the arrows go from one image (icon) to the next image (icon).

2. We would like to have a title on top that would say 'Tarn Voyages Customer Journey', a subtitle in the middle of the circles that would say Customer Journey' and a line on the bottom that would say 'Want to know more? Talk to us today or visit www.bluntore.co.uk.'.

3. I'm also sending some examples of our design that we like and if you could follow the same style that'd be great (the files that are named The Complete Handbook of ...). Please use the colours from these documents or you can use the following ones:
Red: 233, 36, 64
Orange: 238, 87, 37
Light orange: 241, 112, 36
Yellow: 248, 174, 32

4. I've also attached our vector logo.

5. As this is intended for print, please use CMYK. I've attached PSD and INDD templates so you know what the margins are.

We would like to receive this as a PSD or INDD file so we can amend this later. Please note we're using Adobe CS6 so please save the file in a CS6 compatible format.

We're looking forward to receiving your work!

All the best,

Dorota
Updates

Project Deadline Extended
Reason: We are considering turning this into an online infographic so we'd just like to see more designs that would fit both formats. Thanks, Bluntore

Target Market(s)

Medium-sized and large B2B companies in the UK

Industry/Entity Type

Work

Font styles to use
Sans Serif

Colors
eb1f26
f78f20
fece3e

Requirements
Must have
• professional, sleek look, simplicity, must grab attention at first look
Nice to have
• awesome looking icons
Should not have
• bland colours, aged design, grey background

```html
<!DOCTYPE html>
<html lang="en">
<head>
<meta charset="utf-8">
<title>Tarn Voyages Customer Journey – Bluntore</title>
<link rel="stylesheet" href="https://fonts.googleapis.com/css2?family=Carlito:ital,wght@0,400;0,700;1,700&display=swap">
<style>
  :root {
    --red: #e8264a;
    --orange-box: #f8a21c;
    --orange-text: #f7a21b;
    --pink-frame: #e8489b;
    --tile-fill: #f9cdd5;
    --white: #ffffff;
  }
  * { box-sizing: border-box; margin: 0; padding: 0; }
  html, body { width: 1200px; height: 849px; overflow: hidden; background: var(--white); }
  body { font-family: "Carlito", "Calibri", Arial, sans-serif; }

  .canvas {
    position: relative;
    width: 1200px; height: 849px;
    border: 2px dashed var(--pink-frame);
    background: var(--white);
    overflow: hidden;
  }
  .inner-frame {
    position: absolute; left: 14px; top: 17px; width: 1166px; height: 809px;
    border: 1.5px dashed var(--orange-box);
  }

  .page-title {
    position: absolute; left: 0; top: 26px; width: 100%;
    text-align: center; color: var(--red);
    font-size: 26px; font-weight: 700; line-height: 1.2;
  }
  .page-footer {
    position: absolute; left: 0; top: 790px; width: 100%;
    text-align: center; color: var(--red);
    font-size: 16px; font-weight: 700; line-height: 1.2;
  }

  .journey {
    position: absolute; left: 0; top: 0; width: 1200px; height: 849px;
    transform: scale(0.88);
    transform-origin: 600px 418px;
  }

  .arrows { position: absolute; left: 0; top: 0; width: 1200px; height: 849px; }

  .stage-box {
    position: absolute;
    background: var(--orange-box);
    color: var(--white);
    padding: 9px 11px;
    font-size: 11.5px;
    line-height: 1.3;
  }
  .stage-box h2 { font-size: 14px; font-weight: 700; line-height: 1.15; }
  .stage-box .lead { font-weight: 700; margin-bottom: 7px; }
  .stage-box ul { list-style: none; padding-left: 22px; font-weight: 700; }
  .stage-box li { position: relative; margin-bottom: 1px; }
  .stage-box li::before {
    content: ""; position: absolute; left: -18px; top: 5px;
    width: 4px; height: 4px; background: var(--white);
  }
  .stage-box .columns { display: flex; gap: 18px; }

  .box-enquiry { left: 128px; top: 26px; width: 278px; height: 121px; }
  .box-quote { left: 791px; top: 31px; width: 281px; height: 107px; }
  .box-book { left: 943px; top: 214px; width: 228px; height: 188px; }
  .box-holiday { left: 943px; top: 442px; width: 228px; height: 91px; }
  .box-post { left: 368px; top: 701px; width: 470px; height: 105px; }
  .box-consideration { left: 47px; top: 432px; width: 211px; height: 140px; }
  .box-brochure { left: 47px; top: 214px; width: 211px; height: 170px; }

  .stage-icon {
    position: absolute; width: 93px; height: 93px;
    border: 4px solid var(--red); border-radius: 6px;
    background: var(--tile-fill);
  }
  .icon-request { left: 435px; top: 26px; }
  .icon-receive { left: 661px; top: 28px; }
  .icon-book { left: 812px; top: 221px; }
  .icon-holiday { left: 791px; top: 445px; }
  .icon-post { left: 559px; top: 559px; width: 101px; height: 101px; border-color: #c81e3c; }
  .icon-consider { left: 302px; top: 445px; }
  .icon-new { left: 281px; top: 221px; }

  .stage-label {
    position: absolute; width: 170px; margin-left: -85px;
    text-align: center; color: var(--red);
    font-style: italic; font-weight: 700; font-size: 15.5px; line-height: 1.2;
  }
  .label-request { left: 481px; top: 126px; }
  .label-receive { left: 707px; top: 143px; }
  .label-book { left: 858px; top: 336px; }
  .label-holiday { left: 837px; top: 557px; }
  .label-post { left: 609px; top: 669px; }
  .label-consider { left: 348px; top: 557px; }
  .label-new { left: 327px; top: 333px; }

  .centre-title {
    position: absolute; left: 448px; top: 286px; width: 300px;
    text-align: center; color: var(--orange-text);
    font-size: 50px; font-weight: 400; line-height: 1.3;
  }

  .brand-name {
    position: absolute; left: 1015px; top: 752px;
    color: var(--red); font-size: 40px; font-weight: 400; line-height: 1;
  }
</style>
</head>
<body>
<main class="canvas">
  <div class="inner-frame"></div>

  <h1 class="page-title">Tarn Voyages Customer Journey</h1>

  <div class="journey">
    <svg class="arrows" viewBox="0 0 1200 849" aria-hidden="true">
      <defs>
        <marker id="arrowhead" markerWidth="8" markerHeight="8" refX="5" refY="4" orient="auto" markerUnits="strokeWidth">
          <path d="M0,0 L8,4 L0,8 Z" fill="#f8a21c"/>
        </marker>
      </defs>
      <g fill="none" stroke="#f8a21c" stroke-width="4" stroke-linecap="round" marker-end="url(#arrowhead)">
        <path d="M398 205 Q404 180 424 165"/>
        <path d="M560 100 Q608 88 650 96"/>
        <path d="M777 165 Q812 175 823 205"/>
        <path d="M856 385 Q858 408 848 428"/>
        <path d="M777 552 Q732 590 682 600"/>
        <path d="M548 598 Q472 590 414 555"/>
        <path d="M345 428 Q340 402 343 382"/>
      </g>
    </svg>

    <section class="stage-box box-enquiry">
      <h2>ENQUIRY</h2>
      <p class="lead">Ensure individual approach to customers via:</p>
      <ul>
        <li>Single customer view</li>
        <li>Process enquiries based on best practice</li>
        <li>Task creation for manual follow-up</li>
      </ul>
    </section>

    <section class="stage-box box-quote">
      <h2>QUOTE</h2>
      <p class="lead">Send timely personalised proposals via<br>:</p>
      <ul>
        <li>Pipeline management</li>
        <li>Communication tracking</li>
      </ul>
    </section>

    <section class="stage-box box-book">
      <h2>BOOK</h2>
      <p class="lead">Up-sell &amp; cross-sell via:</p>
      <ul>
        <li>Deliver great service based on their preference</li>
        <li>Suggest options based on their history</li>
        <li>Run a targeted nurture program to cross- and up-sell</li>
        <li>Single customer view</li>
      </ul>
    </section>

    <section class="stage-box box-holiday">
      <h2>ON HOLIDAY</h2>
      <p class="lead">Create the perfect experience via:</p>
      <ul>
        <li>Case management</li>
      </ul>
    </section>

    <section class="stage-box box-post">
      <h2>POST-TRAVEL</h2>
      <p class="lead">Make sure customers love you via:</p>
      <div class="columns">
        <ul>
          <li>Review capture</li>
          <li>Targeted email nurture campaigns</li>
        </ul>
        <ul>
          <li>Complaint handling</li>
          <li>Proactive surveys for feedback</li>
        </ul>
      </div>
    </section>

    <section class="stage-box box-consideration">
      <h2>CONSIDERATION</h2>
      <p class="lead">Retain your customers via:</p>
      <ul>
        <li>Ongoing email nurture based on previous history</li>
        <li>Targeted follow-up</li>
      </ul>
    </section>

    <section class="stage-box box-brochure">
      <h2>BROCHURE</h2>
      <p class="lead">Improve customer targeting via:</p>
      <ul>
        <li>Segmented database</li>
        <li>Targeted email nurture</li>
        <li>Following best practice that's embedded in your system</li>
        <li>Website analytics</li>
      </ul>
    </section>

    <div class="stage-icon icon-request" role="img" aria-label="Icon: person sending a message to request more information"></div>
    <div class="stage-icon icon-receive" role="img" aria-label="Icon: person on the phone receiving offers"></div>
    <div class="stage-icon icon-book" role="img" aria-label="Icon: person cheering after booking the holiday"></div>
    <div class="stage-icon icon-holiday" role="img" aria-label="Icon: person on a beach with palm tree and sun"></div>
    <div class="stage-icon icon-post" role="img" aria-label="Icon: person at home after the holiday"></div>
    <div class="stage-icon icon-consider" role="img" aria-label="Icon: person thinking about an island getaway"></div>
    <div class="stage-icon icon-new" role="img" aria-label="Icon: person reading a brochure"></div>

    <p class="stage-label label-request">Request more<br>information</p>
    <p class="stage-label label-receive">Receive offers</p>
    <p class="stage-label label-book">Book the<br>holiday</p>
    <p class="stage-label label-holiday">Go on holiday</p>
    <p class="stage-label label-post">Post-holiday</p>
    <p class="stage-label label-consider">Consider going<br>again</p>
    <p class="stage-label label-new">New Customer</p>

    <h2 class="centre-title">Customer<br>Journey</h2>

    <p class="brand-name">Bluntore</p>
  </div>

  <p class="page-footer">Want to know more? Talk to us today or visit www.bluntore.co.uk.</p>
</main>
</body>
</html>
```